Flyer-Design für Schwimmtraining für Triathleten
Zielgruppe
Angebot
Schwimmen: als Personal Training, in Kleingruppen oder im Kraulkurs
Schwimmen: Videoanalysen
Triathlon: Trainingspläne, Leistungsdiagnostik
Zielgruppe des Flyers:
Triathleten jeder Leistungsklasse
Flyer ist a) als Auslage in Sportgeschäften, b) als Beilage in Wettkampftüten von Triathlonwettkämpfen gedacht
Aufgabenstellung
Triathleten sind tendenziell technisch orientierte Menschen, vergleichsweise wohlhabend. Schwimmen ist häufig eher die verhasste aber notwendige Teil der drei Disziplinen.
Bitte kein Standardformat für den Flyer.
Die Herausforderung bei einem Flyer als Beigabe zum Wettkampfbeutel: Überlicherweise wird der ganze Packen Werbung achtlos weggeworfen. Design und Format sollen dazu beitragen, dass der Flyer heraussticht und möglichst beachtet wird.
Grundsätzliche Infos: www.kelp42.de

```html
<!DOCTYPE html>
<html lang="de">
<head>
<meta charset="utf-8">
<title>Flyer Schwimm- und Triathlontraining</title>
<link rel="stylesheet" href="https://fonts.googleapis.com/css2?family=Righteous&family=Open+Sans:ital,wght@0,400;1,400;1,700&display=swap">
<style>
  :root {
    --page-bg: #c4e0fb;
    --bar-blue: #1e96e0;
    --white: #ffffff;
    --ink: #1b1b1b;
    --lake-top: #3a7f96;
    --lake-mid: #2a6a86;
    --lake-bottom: #1b4a68;
    --portrait-light: #f4f4f4;
    --portrait-tone: #d9c2ae;
  }
  * { margin: 0; padding: 0; box-sizing: border-box; }
  html, body { width: 1200px; height: 1200px; overflow: hidden; }
  body { background: var(--page-bg); font-family: "Open Sans", Arial, sans-serif; position: relative; }

  .flyer { position: absolute; left: 60px; width: 1080px; height: 540px; overflow: hidden; }
  .flyer--front { top: 40px; }
  .flyer--back { top: 620px; background: var(--white); }

  .lake-photo {
    position: absolute; inset: 0;
    background: linear-gradient(180deg, var(--lake-top) 0%, var(--lake-mid) 50%, var(--lake-bottom) 100%);
  }

  .bar {
    position: absolute; background: var(--bar-blue); color: var(--white);
    font-family: "Righteous", "Arial Black", sans-serif; text-transform: uppercase;
    display: flex; align-items: center; justify-content: center; white-space: nowrap;
  }
  .bar--slogan { font-size: 54px; letter-spacing: 3px; text-shadow: 2px 2px 0 rgba(0,0,0,0.18); }
  .bar--make { left: 354px; top: 198px; width: 521px; height: 124px; }
  .bar--friend { left: 517px; top: 372px; width: 563px; height: 130px; }

  .bar--title { font-size: 38px; letter-spacing: 4px; justify-content: flex-start; padding-left: 36px; }
  .bar--schwimm { left: 0; top: 46px; width: 403px; height: 87px; }
  .bar--triathlon { left: 139px; top: 149px; width: 521px; height: 87px; }

  .back-copy { position: absolute; left: 139px; top: 262px; width: 600px; color: var(--ink); }
  .back-copy__question { font-size: 22px; font-weight: 700; font-style: italic; line-height: 29px; letter-spacing: 1px; }
  .back-copy__intro { margin-top: 30px; font-size: 16px; line-height: 21px; letter-spacing: 0.5px; }
  .back-copy__contact { margin-top: 36px; font-size: 13px; letter-spacing: 0.3px; }
  .back-copy__contact strong { font-style: italic; font-weight: 700; }

  .trainer-portrait {
    position: absolute; left: 765px; top: 50px; width: 248px; height: 490px;
    background: linear-gradient(180deg, var(--portrait-light) 0%, var(--portrait-tone) 55%, var(--portrait-light) 100%);
    border-radius: 110px 110px 0 0;
  }
</style>
</head>
<body>
  <section class="flyer flyer--front">
    <div class="lake-photo" role="img" aria-label="Foto: Schwimmer im Freiwasser auf einem Bergsee mit Bergen und Wolkenhimmel, blau getönt"></div>
    <div class="bar bar--slogan bar--make">Make Water</div>
    <div class="bar bar--slogan bar--friend">Your Friend!</div>
  </section>

  <section class="flyer flyer--back">
    <div class="bar bar--title bar--schwimm">Schwimm- und</div>
    <div class="bar bar--title bar--triathlon">Triathlontraining</div>
    <div class="back-copy">
      <p class="back-copy__question">Du suchst einen kompetenten Trainer<br>für Schwimmen oder Triathlon?</p>
      <p class="back-copy__intro">Mein Name ist Lars Brenning und dein Training bei mir profitiert nicht nur von vier Jahrzehnten persönlicher Wettkampferfahrung im Schwimm-, Triathlon- und Laufsport, sondern ebenso von meinen vielfältigen Ausbildungen zum Trainer, Ernährungsberater und systemischen Körpercoach.</p>
      <p class="back-copy__contact"><strong>Lars Brenning</strong> 0151-23456789 | www.kelp42.de | lars@kelp42.de</p>
    </div>
    <div class="trainer-portrait" role="img" aria-label="Foto: Trainer in Badehose mit Badekappe, Schwimmbrille und gelbem Pullbuoy"></div>
  </section>
</body>
</html>
```